BQN Project Signage

Need a sign to be displayed in the front of properties currently under Construction or Renovation to advertise our company information. Need it to be Professional and Contemporary. We are a Design/Build Construction Company. Information should include Company Name, email, website, phone number. Attached: Logo and company brochure, also included and inspiration images

```html
<!DOCTYPE html>
<html lang="en">
<head>
<meta charset="utf-8">
<title>BQN Construction Project Sign</title>
<link rel="stylesheet" href="https://fonts.googleapis.com/css2?family=Bebas+Neue&family=Poppins:wght@400;500;600;700&display=swap">
<style>
  :root {
    --backdrop: #9aa1a8;
    --sign-white: #ffffff;
    --ink: #111111;
    --panel-dark: #0b0b0b;
    --panel-mid: #1c1c1c;
    --accent: #e6e024;
    --text-light: #ffffff;
  }
  * { margin: 0; padding: 0; box-sizing: border-box; }
  html, body {
    width: 1200px; height: 2400px; overflow: hidden;
    background: var(--backdrop);
  }
  .sign {
    position: absolute; left: 80px; top: 420px;
    width: 1040px; height: 1560px;
    background: var(--sign-white);
    box-shadow: 0 20px 50px rgba(0,0,0,.35);
    overflow: hidden;
    font-family: "Poppins", sans-serif;
  }
  .brand {
    position: absolute; top: 176px; left: 0; width: 100%;
    display: flex; justify-content: center; align-items: center; gap: 18px;
    font-family: "Poppins", sans-serif; font-weight: 500;
    font-size: 50px; letter-spacing: 2px; color: var(--ink);
  }
  .brand-dot {
    width: 40px; height: 40px; border-radius: 50%; background: var(--accent);
  }
  .owner-name {
    position: absolute; top: 368px; left: 0; width: 100%;
    text-align: center;
    font-family: "Bebas Neue", sans-serif; font-size: 196px; line-height: 1;
    color: var(--ink); letter-spacing: 1px;
  }
  .contact-panel {
    position: absolute; left: 0; top: 640px; width: 100%; height: 787px;
    background: linear-gradient(170deg, var(--panel-mid), var(--panel-dark) 60%);
  }
  .role-band {
    position: absolute; left: 146px; top: 588px; width: 741px; height: 87px;
    background: var(--accent);
    display: flex; align-items: center; justify-content: center;
    font-weight: 500; font-size: 54px; letter-spacing: 4px; color: var(--ink);
  }
  .icon-row { position: absolute; left: 0; top: 768px; width: 100%; height: 100px; }
  .address, .email {
    position: absolute; left: 0; width: 100%; text-align: center;
    color: var(--text-light); font-weight: 400;
  }
  .address { top: 878px; font-size: 58px; line-height: 70px; }
  .email { top: 1060px; font-size: 58px; }
  .mobile {
    position: absolute; left: 0; top: 1225px; width: 100%;
    display: flex; justify-content: center; align-items: center; gap: 16px;
    color: var(--text-light); font-weight: 700; font-size: 110px; line-height: 1;
  }
  .office-band {
    position: absolute; left: 92px; top: 1395px; width: 848px; height: 87px;
    background: var(--accent);
    display: flex; align-items: center; justify-content: center; gap: 18px;
    color: var(--ink); font-weight: 700; font-size: 64px;
  }
  .office-label { font-weight: 700; letter-spacing: 1px; }
  .office-number { font-weight: 600; }
</style>
</head>
<body>
  <main class="sign">
    <div class="brand"><span class="brand-dot"></span><span class="brand-name">BQN CONSTRUCTION</span></div>
    <h1 class="owner-name">MARCUS DELRAY</h1>

    <div class="contact-panel" role="img" aria-label="Dark photograph of a building under construction"></div>

    <div class="role-band">DESIGN &amp; BUILDER</div>

    <svg class="icon-row" viewBox="0 0 1040 100" width="1040" height="100" aria-hidden="true">
      <g stroke="#e6e024" stroke-width="3">
        <line x1="255" y1="48" x2="404" y2="48"/>
        <line x1="305" y1="58" x2="404" y2="58"/>
        <line x1="626" y1="48" x2="772" y2="48"/>
        <line x1="626" y1="58" x2="722" y2="58"/>
      </g>
      <circle cx="450" cy="50" r="46" fill="#e6e024"/>
      <path d="M450 20c-14 0-24 10-24 23 0 17 24 39 24 39s24-22 24-39c0-13-10-23-24-23z" fill="#111"/>
      <circle cx="450" cy="43" r="9" fill="#e6e024"/>
      <circle cx="580" cy="50" r="46" fill="#e6e024"/>
      <rect x="555" y="34" width="50" height="34" fill="none" stroke="#111" stroke-width="4"/>
      <path d="M555 34l25 20 25-20M555 68l18-16M605 68l-18-16" fill="none" stroke="#111" stroke-width="4"/>
    </svg>

    <p class="address">4815 Harbor View Rd., Ste. 108<br>Cedar Point, FL 32901</p>
    <p class="email">nora@bqnconstruction.com</p>

    <div class="mobile">
      <svg width="100" height="100" viewBox="0 0 100 100" aria-hidden="true">
        <circle cx="50" cy="50" r="50" fill="#e6e024"/>
        <path d="M34 24l10 14-6 7c4 8 10 14 18 18l7-6 14 10-6 10c-22 2-48-24-47-47z" fill="#111"/>
      </svg>
      <span class="mobile-number">555.210.3846</span>
    </div>

    <div class="office-band">
      <span class="office-label">OFFICE</span>
      <svg width="62" height="62" viewBox="0 0 100 100" aria-hidden="true">
        <circle cx="50" cy="50" r="44" fill="none" stroke="#111" stroke-width="8"/>
        <path d="M36 28l9 12-5 6c3 7 8 12 15 15l6-5 12 9-5 8c-19 2-40-20-39-39z" fill="#111"/>
      </svg>
      <span class="office-number">555.210.7720</span>
    </div>
  </main>
</body>
</html>
```